NURSING: STEP BEYOND THE HEDGEROW

Size of the book cover: 140 x 215 mms

I need a cover for the 30,000 word book I have just written. It is a positive take on what I think nursing is and what it needs to be in the future. It is also my story of being nursed and of being a nurse.

My dream is that nurses honor themselves; that they look to the future with confidence and intelligence and that care continues to be delivered with compassionate person centeredness.

I define nursing as a professional workforce which, with probity, prevent or relieve distress; provide compassionate, safe, excellent care; and which contributes to the organization of healthcare.

The name comes from a Biblical parable Mathew 5:14-16. If a light is hidden under a bushel (basket) it is barely seen. If it is lit out from the basket it is clearly seen. As nurses we must continue to take up our mantel and ensure our light is seen and that it continues to shine the way we want it to.

As nurses we each take up our own lantern of caring, each in our own ways. To walk more brightly in our own paths of service.

The final design should show the specialness of nursing.

Target Market(s)

Nurses present, past and future

Industry/Entity Type

Healthcare

Font styles to use
Sans Serif
Other font styles liked:
• Whatever you think will suit

Colors
ec1f27
0393ce
9bcb3c

Requirements
Must have
• Be friendly, calming.
• NB: I am not sure whether the title should be in uppercase or not. Nursing could be uppercase and step beyond the hedgerow could be lower case. I leave it to you experienced people
Nice to have
• Something that depicts nursing...or is suggestive of nursing and the specialness of the work we do. How we bring our light to our patients as we 'hold them in the palms of out hands' and care for them. How they honor us by allowing us into their lives. Our rich past and out history allows us to be who we are today and we look to the future with confidence and hope
• I like rich colors, eg the color type you might find on a stained glass window in a church - rich emerald green or rich crimson red or the deep blue of a nurses cape
Should not have
• A dark cover
• clutter
• Religious overtone
• I have chosen three colors but they are not in the shading I would like - see above

```html
<!DOCTYPE html>
<html lang="en">
<head>
<meta charset="utf-8">
<title>Nursing: Step Beyond The Hedgerow — Book Cover</title>
<link href="https://fonts.googleapis.com/css2?family=Allura&family=Lato:wght@400;700&family=Lora:ital,wght@0,400;0,700;1,400&display=swap" rel="stylesheet">
<style>
  :root {
    --page-bg: #eceef1;
    --paper: #ffffff;
    --title-blue: #4a7cc0;
    --band-blue: #5a8fd2;
    --spine-blue: #34568c;
    --pale-blue: #bccde9;
    --mid-blue: #4f82c6;
    --slate: #5a5e65;
    --ink-soft: #6e7580;
    --spine-script: #9fb6db;
  }
  * { margin: 0; padding: 0; box-sizing: border-box; }
  html, body { width: 1200px; height: 933px; overflow: hidden; }
  body { background: var(--page-bg); font-family: "Lora", Georgia, serif; }

  .book-wrap { position: absolute; left: 85px; top: 86px; width: 1030px; height: 760px; display: flex; box-shadow: 0 10px 30px rgba(40,50,70,.15); }

  .back-cover, .front-cover { position: relative; width: 495px; height: 760px; background: var(--paper); overflow: hidden; }
  .spine { position: relative; width: 40px; height: 760px; background: var(--spine-blue); }
  .spine-title { position: absolute; left: 50%; top: 50%; transform: translate(-50%, -50%) rotate(90deg); font-family: "Allura", cursive; font-size: 46px; color: var(--spine-script); white-space: nowrap; }

  .shape-layer { position: absolute; inset: 0; width: 100%; height: 100%; }

  /* Back cover */
  .back-lead { position: absolute; left: 40px; top: 42px; width: 420px; font-size: 14.5px; line-height: 1.3; color: var(--ink-soft); }
  .back-aside { position: absolute; font-size: 10px; line-height: 1.35; }
  .back-aside.pale { right: 28px; top: 240px; width: 150px; color: var(--mid-blue); }
  .back-aside.deep { left: 22px; top: 332px; width: 130px; color: #fff; }
  .back-heading { position: absolute; left: 60px; top: 452px; font-size: 17px; color: var(--slate); }
  .back-body { position: absolute; left: 60px; width: 400px; font-size: 11.5px; line-height: 1.35; color: var(--ink-soft); }
  .back-body.first { top: 476px; }
  .back-body.second { top: 540px; }
  .reviewer-photo { position: absolute; left: 28px; top: 612px; width: 122px; height: 122px; background: linear-gradient(160deg, #e9d7cb, #a9bfe0); }
  .back-band { position: absolute; left: 150px; top: 628px; width: 345px; height: 132px; background: var(--slate); padding: 20px 22px; color: #fff; font-size: 11.5px; line-height: 1.4; }

  /* Front cover */
  .cover-title { position: absolute; left: 22px; top: 8px; font-family: "Allura", cursive; font-size: 128px; line-height: 1; color: var(--title-blue); }
  .cover-subtitle { position: absolute; left: 60px; top: 138px; font-family: "Lato", sans-serif; font-size: 23px; color: var(--title-blue); letter-spacing: .2px; }
  .photo { position: absolute; }
  .photo-team { left: 268px; top: 170px; width: 120px; height: 95px; background: linear-gradient(180deg, #f1f4f8, #cfdaea); }
  .photo-nurse { left: 388px; top: 120px; width: 107px; height: 145px; background: linear-gradient(160deg, #d8c0ae, #8fb0d8); }
  .cover-quote { position: absolute; left: 70px; top: 492px; width: 380px; font-size: 18.5px; line-height: 1.25; color: var(--title-blue); text-align: center; }
  .cover-author { position: absolute; left: 0; right: 0; top: 678px; text-align: center; font-family: "Lora", serif; font-weight: 700; font-size: 26px; color: #fff; }
</style>
</head>
<body>
  <main class="book-wrap">
    <section class="back-cover" aria-label="Back cover">
      <svg class="shape-layer" viewBox="0 0 495 760" aria-hidden="true">
        <polygon points="495,160 495,318 150,318" fill="var(--pale-blue)"/>
        <polygon points="0,292 345,322 0,430" fill="var(--mid-blue)"/>
      </svg>
      <p class="back-lead">"We each take up our own lantern of caring, each in our own ways, to walk more brightly in our own path of service. We each take up our own lantern of caring, each in our own ways, to walk more brightly in our own path of service." We each take up our own lantern of caring, each in our own ways, to walk more brightly in our own path of service.</p>
      <p class="back-aside pale">We each take up our own lantern of caring, each in our own ways, to walk more brightly in our own path of service.</p>
      <p class="back-aside deep">We each take up our own lantern of caring, each in our own ways, to walk more brightly in our own path of service.</p>
      <h2 class="back-heading">"We each take up our own lantern</h2>
      <p class="back-body first">We each take up our own lantern of caring, each in our own ways, to walk more brightly in our own path of service. We each take up our own lanterns of caring, each in our own ways, to walk more brightly in our own path of service.</p>
      <p class="back-body second">We each take up our own lantern of caring, each in our own ways, to walk more brightly in our own path of service. We each take up our own lanterns of caring, each in our own ways, to walk more brightly in our own path of service.</p>
      <div class="reviewer-photo" role="img" aria-label="Photo of a smiling young nurse in blue scrubs"></div>
      <div class="back-band">"We each take up our own lantern of caring, each in our own ways, to walk more brightly in our own path of service. We each take up our own lantern of caring, each in our own ways, to walk more brightly in our own path of service."</div>
    </section>

    <section class="spine" aria-label="Spine">
      <span class="spine-title">Nursing</span>
    </section>

    <section class="front-cover" aria-label="Front cover">
      <svg class="shape-layer" viewBox="0 0 495 760">
        <defs>
          <linearGradient id="care-photo" x1="0" y1="0" x2="1" y2="1">
            <stop offset="0" stop-color="#e4e7ec"/>
            <stop offset=".45" stop-color="#e9c9b3"/>
            <stop offset="1" stop-color="#c99a80"/>
          </linearGradient>
        </defs>
        <polygon points="0,330 200,265 495,265 495,430 260,470 0,470" fill="url(#care-photo)" role="img" aria-label="Photo of a nurse caring for an elderly patient, with a close view of hands held together"/>
        <polygon points="140,300 330,265 230,330" fill="#ffffff" opacity=".75"/>
        <polygon points="0,610 495,588 495,760 0,760" fill="var(--band-blue)"/>
      </svg>
      <h1 class="cover-title">Nursing</h1>
      <p class="cover-subtitle">Step Beyond The Hedgerow</p>
      <div class="photo photo-team" role="img" aria-label="Photo of a group of nurses and doctors"></div>
      <div class="photo photo-nurse" role="img" aria-label="Photo of a smiling nurse with a stethoscope"></div>
      <p class="cover-quote">"We each take up our own lantern of caring, each in our own ways, to walk more brightly in our own path of service</p>
      <p class="cover-author">Maren Holloway</p>
    </section>
  </main>
</body>
</html>
```